RVK Entertainment

Logo for business card design

Target Market(s)

potential film investors and screenwriters

Industry/Entity Type

Business

Contact Information for Business Card

as shown, website here is a placeholder position

Requirements
Must have
• great visual appeal
Nice to have
• harmony of colors; must evoke spirit of
• U.S.-China cooperation

```html
<!DOCTYPE html>
<html lang="en">
<head>
<meta charset="utf-8">
<title>RVK Entertainment — Business Card</title>
<link href="https://fonts.googleapis.com/css2?family=Questrial&display=swap" rel="stylesheet">
<style>
  :root {
    --backdrop: #141a2a;
    --backdrop-edge: #0b0f1a;
    --card-dark: #1b1b1d;
    --card-dark-edge: #2a2a2d;
    --card-light: #ffffff;
    --ink: #1a1a1a;
    --brand-blue: #2a3f9e;
    --brand-red: #e8261c;
    --brand-yellow: #d4cf2c;
    --mark-light: #f2f2f4;
  }
  * { box-sizing: border-box; margin: 0; padding: 0; }
  html, body { width: 1200px; height: 900px; overflow: hidden; }
  body {
    position: relative;
    font-family: "Questrial", "Century Gothic", sans-serif;
    background: radial-gradient(ellipse at 45% 40%, var(--backdrop) 0%, var(--backdrop-edge) 85%);
  }
  .card {
    position: absolute;
    width: 600px;
    height: 330px;
    border-radius: 26px;
    box-shadow: 0 18px 40px rgba(0,0,0,0.55);
  }
  .card--back {
    left: 110px; top: 70px;
    background: linear-gradient(160deg, var(--card-dark-edge), var(--card-dark) 55%);
    display: flex; align-items: center; justify-content: center;
  }
  .card--front {
    left: 290px; top: 420px;
    background: var(--card-light);
  }
  .brand {
    display: flex; align-items: center; gap: 14px;
    font-size: 30px; letter-spacing: 0.06em; line-height: 1;
    white-space: nowrap;
  }
  .brand__square { width: 30px; height: 30px; flex: none; }
  .brand--on-dark { color: var(--brand-yellow); }
  .brand--on-dark .brand__square { background: var(--brand-red); }
  .brand--on-light { color: var(--brand-blue); font-size: 24px; }
  .brand--on-light .brand__square { background: var(--brand-red); width: 24px; height: 24px; }
  .card--front .brand {
    position: absolute; left: 40px; top: 150px;
  }
  .contact {
    position: absolute; left: 360px; top: 78px;
    color: var(--ink);
  }
  .contact__name { font-size: 27px; letter-spacing: 0.02em; }
  .contact__title { font-size: 15px; color: var(--brand-red); margin: 2px 0 12px; }
  .contact__list { list-style: none; }
  .contact__item {
    display: flex; align-items: center; gap: 14px;
    font-size: 16px; margin-bottom: 9px; padding-left: 4px;
  }
  .contact__icon { width: 18px; height: 18px; fill: var(--brand-blue); flex: none; }
  .signature-mark {
    position: absolute; right: 64px; top: 770px;
    color: var(--mark-light);
    font-size: 28px; letter-spacing: 0.06em;
  }
  .signature-mark .brand__square { background: var(--mark-light); width: 28px; height: 28px; }
</style>
</head>
<body>
  <section class="card card--back" aria-label="Card back">
    <div class="brand brand--on-dark">
      <span class="brand__square"></span>
      <span class="brand__name">RVK Entertainment</span>
    </div>
  </section>

  <section class="card card--front" aria-label="Card front">
    <div class="brand brand--on-light">
      <span class="brand__square"></span>
      <span class="brand__name">RVK Entertainment</span>
    </div>
    <div class="contact">
      <p class="contact__name">Your Name</p>
      <p class="contact__title">Job Title</p>
      <ul class="contact__list">
        <li class="contact__item">
          <svg class="contact__icon" viewBox="0 0 20 20" aria-hidden="true"><path d="M2 6c0-2 3-3 8-3s8 1 8 3v2h-4V6.5c-1-.5-2.5-.7-4-.7s-3 .2-4 .7V8H2z"/><path d="M5 9h10l2 8H3z"/></svg>
          <span>000 000 0000</span>
        </li>
        <li class="contact__item">
          <svg class="contact__icon" viewBox="0 0 20 20" aria-hidden="true"><path d="M1 4h18v12H1z"/><path d="M1 4l9 7 9-7" fill="none" stroke="#fff" stroke-width="1.5"/></svg>
          <span>Email@xyz.com</span>
        </li>
        <li class="contact__item">
          <svg class="contact__icon" viewBox="0 0 20 20" aria-hidden="true"><g fill="none" stroke="#2a3f9e" stroke-width="1.4"><circle cx="10" cy="10" r="8"/><ellipse cx="10" cy="10" rx="3.5" ry="8"/><path d="M2 10h16M3.5 6h13M3.5 14h13"/></g></svg>
          <span>website</span>
        </li>
      </ul>
    </div>
  </section>

  <div class="signature-mark brand">
    <span class="brand__square"></span>
    <span class="brand__name">RVK Entertainment</span>
  </div>
</body>
</html>
```